Hollow Breeze - New Product needs a Label

We need a package label for a new project that will come to market soon. The company is based in Canada and will need to show 'Made in Canada' with a Canadian flag.

The product is called Hollow Breeze. It is an odour eliminator. It will be in a dark brown plastic container that can be opened and left open in a room.

It can be used to help eliminate a number of different types of smoke; cigarette, pot or even fireplace smoke. We believe that 'no one should know what you smoke'.

We would like to see designs that reflect the intent of the product - to cover smoke. So far we've only thought that smokey colours like smokey green, smokey lavender and smokey grey or other grey tone colours would make sense. Update: I have removed the image that I 'doodled' on my own because I think it's been taken too literally. Please give me a fresh look at what an odor eliminator image could be.

Label dimensions are 11.25"x2.25"
Key wording:

Product Name: Hollow Breeze
Tag line: No one needs to know what you smoke
Also needs to include:
Directions
Remove the lid and place the container in any room where smoke is present. The contents will evaporate, neutralizing odours.

Net Wt. 14 0z. - 400 G
A spot for adding a bar code for scanners

Target Market(s)

Cigarette smokers / pot smokers / people with fire places or people who share a home with any of those categories

Requirements
Must have
• a label that fits the dimensions 11.25"x2.25" and the text / components outlined in the description
Nice to have
• A bit of humour, a sense of natural products

```html
<!DOCTYPE html>
<html lang="en">
<head>
<meta charset="utf-8">
<title>Hollow Breeze – Label</title>
<link rel="stylesheet" href="https://fonts.googleapis.com/css2?family=Outfit:wght@400;500;600&family=Roboto:wght@400&display=swap">
<style>
  :root {
    --backdrop: #555555;
    --label-white: #ffffff;
    --ink-navy: #2b3354;
    --sage-mist: #d6ded4;
    --flag-red: #d52b1e;
  }
  * { margin: 0; padding: 0; box-sizing: border-box; }
  html, body {
    width: 1200px; height: 1200px; overflow: hidden;
    background: var(--backdrop);
  }
  .label {
    position: absolute;
    left: 50px; top: 490px;
    width: 1100px; height: 220px;
    background: var(--label-white);
    overflow: hidden;
    font-family: "Outfit", sans-serif;
    color: var(--ink-navy);
  }
  .leaf-motif {
    position: absolute; top: 0; height: 220px;
    background: radial-gradient(ellipse at center, var(--sage-mist) 0%, rgba(214,222,212,0.55) 45%, rgba(255,255,255,0) 72%);
  }
  .leaf-motif--left { left: -60px; width: 190px; }
  .leaf-motif--middle { left: 436px; width: 207px; }
  .leaf-motif--right { left: 966px; width: 200px; }

  .product-name {
    position: absolute; left: 118px; top: 22px;
    font-weight: 600; font-size: 88px; line-height: 76px;
    letter-spacing: 1px; text-transform: uppercase;
  }
  .tagline {
    position: absolute; left: 109px; top: 178px; width: 329px;
    border-top: 1px solid var(--ink-navy);
    border-bottom: 1px solid var(--ink-navy);
    font-size: 16px; line-height: 20px; text-align: center;
    padding: 1px 0 0;
    border-bottom-color: rgba(43,51,84,0.6);
  }
  .origin-badge {
    position: absolute; left: 655px; top: 70px;
    height: 28px; padding: 0 8px;
    border: 1px solid var(--ink-navy); border-radius: 2px;
    display: flex; align-items: center; gap: 8px;
    font-family: "Roboto", sans-serif; font-size: 16px;
  }
  .flag { display: block; }
  .directions {
    position: absolute; left: 656px; top: 113px;
    font-size: 11.5px; line-height: 15px;
  }
  .directions-title { margin-bottom: 2px; }
  .net-weight {
    position: absolute; left: 655px; top: 172px;
    font-size: 16px; font-weight: 500; letter-spacing: 0.3px;
  }
</style>
</head>
<body>
  <section class="label">
    <div class="leaf-motif leaf-motif--left" role="img" aria-label="Faint sage outline leaf decoration"></div>
    <div class="leaf-motif leaf-motif--middle" role="img" aria-label="Faint sage outline leaf decoration"></div>
    <div class="leaf-motif leaf-motif--right" role="img" aria-label="Faint sage outline leaf decoration"></div>

    <h1 class="product-name">Hollow<br>Breeze</h1>
    <p class="tagline">No one needs to know what you smoke</p>

    <div class="origin-badge">
      <span>Made in Canada</span>
      <svg class="flag" width="22" height="13" viewBox="0 0 22 13" aria-label="Canadian flag">
        <rect width="22" height="13" fill="#fff"/>
        <rect width="5.5" height="13" fill="var(--flag-red)"/>
        <rect x="16.5" width="5.5" height="13" fill="var(--flag-red)"/>
        <path d="M11 3 L12.6 6.2 L14 5.6 L13.2 8.6 L11.4 8.4 L11.4 10.5 L10.6 10.5 L10.6 8.4 L8.8 8.6 L8 5.6 L9.4 6.2 Z" fill="var(--flag-red)"/>
      </svg>
    </div>

    <div class="directions">
      <p class="directions-title">Directions for use</p>
      <p>Remove the lid and place the container in any room<br>where smoke is present. The contents will evaporate, neutralizing odours.</p>
    </div>

    <p class="net-weight">Net Wt. 14 0z. - 400 G</p>
  </section>
</body>
</html>
```